Clara Dunmore: Adult Models Flyer

We need an attractive flyer design to promote our adult modeling agency and recruit models to our business. We hire beautiful, young women and couples to be on a live adult camshow. We would like to highlight the following features of this job position:

-Pays $100/hour
-Set your own schedule
-Have fun and get paid
-Sign up at cdadultmodels.com

The theme should be similar to the website (hot pink and white). We are putting these flyers around college campuses and nightclubs.
Updates

Just uploaded a couple pics of me and my new model that might work well on the flyer(:

Target Market(s)

Our audience is attractive, young women (college students, baristas, waitresses etc.)

Industry/Entity Type

College

Requirements
Must have
• A picture of Clara Dunmore. Perhaps a long body shot on the side or just her face somewhere. Pictures can be found here: https://chirpline.com/DunmoreClara
and here: http://picvault.io/dunmoreclara

A visible and bold area featuring: "$100/hour"

```html
<!DOCTYPE html>
<html lang="en">
<head>
<meta charset="utf-8">
<title>Clara Dunmore Adult Models – Recruitment Flyer</title>
<link href="https://fonts.googleapis.com/css2?family=Roboto+Condensed:ital,wght@1,700&family=Caveat:wght@400;600&family=Playfair+Display:wght@900&display=swap" rel="stylesheet">
<style>
  :root {
    --ink: #000000;
    --paper: #ffffff;
    --hot-pink: #ec2a8a;
    --pool-light: #6fc3e8;
    --pool-deep: #1f7fb8;
    --warm-skin: #d9a98a;
    --warm-shadow: #6b4a3a;
  }
  * { margin: 0; padding: 0; box-sizing: border-box; }
  html, body { width: 927px; height: 1200px; overflow: hidden; background: var(--ink); }
  .flyer { position: relative; width: 927px; height: 1200px; background: var(--ink); overflow: hidden; }

  .tagline {
    position: absolute;
    color: var(--paper);
    font-family: "Roboto Condensed", "Arial Narrow", sans-serif;
    font-style: italic; font-weight: 700;
    white-space: nowrap;
  }
  .tagline--schedule { left: 92px; top: 92px; font-size: 28px; transform: rotate(5deg); transform-origin: left center; }
  .tagline--fun { left: 68px; top: 398px; font-size: 28px; transform: rotate(-4deg); transform-origin: left center; }
  .tagline--signup { left: 512px; top: 640px; font-size: 31px; transform: rotate(5deg); transform-origin: left center; }

  .card { position: absolute; }
  .card__back { position: absolute; background: var(--hot-pink); }
  .card__front { position: absolute; display: flex; background: var(--paper); }

  .quote {
    font-family: "Caveat", cursive;
    line-height: 1.05;
  }
  .quote__mark {
    font-family: "Playfair Display", Georgia, serif;
    font-weight: 900;
    font-size: 44px;
    line-height: 0;
    vertical-align: -15px;
    color: var(--ink);
  }
  .quote__author { display: block; font-family: "Caveat", cursive; font-style: normal; color: var(--hot-pink); text-align: right; }

  /* top card */
  .card--pool { left: 395px; top: 62px; width: 450px; height: 370px; transform: rotate(6deg); }
  .card--pool .card__back { left: 0; top: 0; width: 420px; height: 350px; }
  .card--pool .card__front { left: 20px; top: 50px; width: 430px; height: 265px; padding: 6px; background: var(--hot-pink); }
  .card--pool .quote-col {
    width: 200px; background: var(--paper); padding: 18px 10px 12px 14px;
    display: flex; flex-direction: column; justify-content: space-between;
  }
  .card--pool .quote { color: var(--hot-pink); font-size: 30px; }
  .card--pool .quote__author { font-size: 26px; }
  .photo--pool { flex: 1; background: linear-gradient(160deg, #a9d4ea 0%, var(--pool-light) 35%, var(--pool-deep) 100%); }

  /* starburst */
  .burst { position: absolute; left: 40px; top: 408px; width: 820px; height: 230px; }
  .burst__price {
    position: absolute; left: 258px; top: 82px;
    color: var(--paper);
    font-family: "Roboto Condensed", "Arial Narrow", sans-serif;
    font-style: italic; font-weight: 700; font-size: 54px;
    transform: rotate(-5deg); white-space: nowrap;
  }

  /* bottom card */
  .card--models { left: 52px; top: 700px; width: 500px; height: 350px; transform: rotate(-5deg); }
  .card--models .card__back { left: 0; top: 0; width: 490px; height: 340px; }
  .card--models .card__front { left: 20px; top: 32px; width: 470px; height: 272px; padding: 8px; gap: 8px; }
  .card--models .quote-col {
    width: 222px; display: flex; flex-direction: column; justify-content: flex-end; padding-bottom: 4px;
  }
  .card--models .quote {
    background: var(--hot-pink); color: var(--paper);
    font-size: 22px; padding: 16px 10px 12px 10px;
  }
  .card--models .quote__author { font-size: 26px; margin-top: 8px; text-align: center; }
  .photo--models { flex: 1; height: 200px; background: linear-gradient(120deg, var(--warm-shadow) 0%, var(--warm-skin) 45%, var(--hot-pink) 80%, var(--warm-shadow) 100%); }

  /* brand card */
  .brand-card {
    position: absolute; left: 612px; top: 830px; width: 262px; height: 190px;
    background: var(--paper); transform: rotate(-8deg);
    display: flex; align-items: center; justify-content: center; gap: 10px;
  }
  .brand-card__dot { width: 18px; height: 18px; border-radius: 50%; background: var(--hot-pink); }
  .brand-card__name {
    color: var(--hot-pink);
    font-family: "Roboto Condensed", "Arial Narrow", sans-serif;
    font-style: italic; font-weight: 700; font-size: 30px;
  }
</style>
</head>
<body>
<main class="flyer">
  <p class="tagline tagline--schedule">Set your own schedule</p>

  <div class="card card--pool">
    <div class="card__back"></div>
    <div class="card__front">
      <div class="quote-col">
        <blockquote class="quote">
          <span class="quote__mark">“</span>Life doesnt have to be hard. It can be fun... and easy!<span class="quote__mark">”</span>
        </blockquote>
        <cite class="quote__author">-Clara Dunmore</cite>
      </div>
      <div class="photo--pool" role="img" aria-label="Full-body photo of Clara Dunmore in a pink and white bikini beside a swimming pool"></div>
    </div>
  </div>

  <p class="tagline tagline--fun">Have fun and get paid</p>

  <div class="burst">
    <svg width="820" height="230" viewBox="0 0 820 230" aria-hidden="true">
      <polygon fill="var(--hot-pink)" points="0,205 220,148 172,100 268,104 242,24 335,74 392,0 420,62 530,18 512,80 790,12 572,114 812,140 570,156 700,222 478,176 456,228 392,182 305,224 310,178 148,212 232,168"/>
    </svg>
    <p class="burst__price">“$100.00 / hour”</p>
  </div>

  <p class="tagline tagline--signup">Sign-up at : cdadultmodels.com</p>

  <div class="card card--models">
    <div class="card__back"></div>
    <div class="card__front">
      <div class="quote-col">
        <blockquote class="quote">
          <span class="quote__mark">“</span>Young women today are afraid of their sexuality... theyre scared to express themselves. Im here to change that<span class="quote__mark">”</span>
        </blockquote>
        <cite class="quote__author">-Clara Dunmore</cite>
      </div>
      <div class="photo--models" role="img" aria-label="Photo of two models in pink bikinis at a party"></div>
    </div>
  </div>

  <div class="brand-card">
    <span class="brand-card__dot"></span>
    <span class="brand-card__name">Clara Dunmore</span>
  </div>
</main>
</body>
</html>
```